Modern Billboard Ad for Criminal Defense Firm

10.5 x 36 We're looking for something to set us apart from the local competition. Looking for sleek and modern. We're a mid-sized firm in a small market city. We want to give the artist room to be creative on this one.
Thanks

Target Market(s)

Adult clients who have been charged with a crime/DWI

Industry/Entity Type

legal

Font styles to use
Serif
Sans Serif

Requirements
Must have
• Needs to have the firm name in large lettering. Law Offices of Marcus T Whitfield. “PLLC” does not have to be included. Phone number of (555) 384-1927 should be included but not the main focus.
Nice to have
• A call to action or something similar. “Don’t go it alone, call today.”, “ Arrested?”

```html
<!DOCTYPE html>
<html lang="en">
<head>
<meta charset="UTF-8">
<title>Law Offices of Marcus T Whitfield – Billboard</title>
<link href="https://fonts.googleapis.com/css2?family=Montserrat:wght@400;500;800&display=swap" rel="stylesheet">
<style>
  :root {
    --page-bg: #e4e5e7;
    --brand-blue: #12a9ea;
    --ink: #252525;
    --panel-light: #ffffff;
    --panel-shade: #ececec;
    --badge-dark: #2b2f38;
    --badge-blue: #1f8fd6;
    --photo-deep: #3a2a22;
    --photo-mid: #6b5a45;
    --photo-light: #9aa08a;
  }
  html, body {
    margin: 0;
    width: 1200px;
    height: 1200px;
    overflow: hidden;
    background: var(--page-bg);
  }
  .billboard {
    position: absolute;
    left: 50px;
    top: 440px;
    width: 1100px;
    height: 321px;
    overflow: hidden;
    background: radial-gradient(ellipse at 40% 55%, var(--panel-light) 30%, var(--panel-shade) 100%);
    font-family: "Montserrat", sans-serif;
    color: var(--ink);
  }
  .billboard-art {
    position: absolute;
    inset: 0;
  }
  .award-badge {
    position: absolute;
    left: 23px;
    top: 18px;
    width: 85px;
    height: 121px;
    background: var(--panel-light);
    box-sizing: border-box;
    padding: 4px;
  }
  .award-badge-body {
    width: 100%;
    height: 100%;
    background: linear-gradient(180deg, var(--badge-blue) 0 18%, var(--badge-dark) 18% 84%, var(--badge-blue) 84%);
  }
  .firm-name {
    position: absolute;
    left: 133px;
    top: 0;
    width: 600px;
    height: 93px;
    margin: 0;
    display: flex;
    align-items: center;
    justify-content: center;
    color: var(--panel-light);
    font-weight: 800;
    font-size: 29px;
    letter-spacing: -0.2px;
    text-transform: uppercase;
    white-space: nowrap;
  }
  .message {
    position: absolute;
    left: 233px;
    top: 98px;
    width: 400px;
    text-align: center;
  }
  .headline {
    margin: 0;
    font-weight: 800;
    font-size: 62px;
    line-height: 66px;
    letter-spacing: 0.5px;
  }
  .tagline {
    margin: 0;
    font-weight: 400;
    font-size: 27px;
    line-height: 34px;
  }
  .cta {
    display: inline-block;
    margin-top: 6px;
    padding: 0 18px;
    height: 40px;
    line-height: 40px;
    border-radius: 10px;
    background: var(--brand-blue);
    color: var(--panel-light);
    font-weight: 500;
    font-size: 28px;
  }
  .phone {
    margin: 6px 0 0;
    font-weight: 500;
    font-size: 30px;
    line-height: 40px;
  }
</style>
</head>
<body>
  <section class="billboard">
    <svg class="billboard-art" width="1100" height="321" viewBox="0 0 1100 321">
      <defs>
        <linearGradient id="photoTone" x1="0" y1="0" x2="1" y2="1">
          <stop offset="0" stop-color="var(--photo-mid)"/>
          <stop offset="0.5" stop-color="var(--photo-deep)"/>
          <stop offset="1" stop-color="var(--photo-light)"/>
        </linearGradient>
      </defs>
      <rect class="name-band" x="0" y="0" width="820" height="93" fill="var(--brand-blue)"/>
      <circle class="portrait-ring" cx="965" cy="166" r="216" fill="var(--brand-blue)"/>
      <circle class="portrait-ring-gap" cx="965" cy="166" r="206" fill="var(--panel-light)"/>
      <g role="img" aria-label="Portrait photo of the attorney in a grey suit, smiling, in front of foliage">
        <circle cx="965" cy="166" r="202" fill="url(#photoTone)"/>
      </g>
    </svg>

    <div class="award-badge" role="img" aria-label="Community award badge">
      <div class="award-badge-body"></div>
    </div>

    <h1 class="firm-name">Law Offices of Marcus T Whitfield</h1>

    <div class="message">
      <h2 class="headline">ARRESTED?</h2>
      <p class="tagline">Don’t Go It Alone,</p>
      <span class="cta">Call Today</span>
      <p class="phone">(555) 384-1927</p>
    </div>
  </section>
</body>
</html>
```